Business Card Design

We require a business card design for a law firm, our signature colours are maroon and cream. Our slogan is "From our family to yours", we would like the cards to be professional however feminine at the same time.

Industry/Entity Type

Business

Contact Information for Business Card

Helena Brackett & Associates Lawyers & Conveyancers, Helena Brackett LL.B. Principal Solicitor, 17 Quillon Street, Marrowdale NSW 2190

Logo styles of interest
Emblem Logo
Abstract Logo
Wordmark Logo

```html
<!DOCTYPE html>
<html lang="en">
<head>
<meta charset="utf-8">
<title>Helena Brackett &amp; Associates – Business Card</title>
<link rel="stylesheet" href="https://fonts.googleapis.com/css2?family=Libre+Baskerville:wght@700&family=Noto+Sans:wght@400&display=swap">
<style>
  :root {
    --cream-light: #fdfbf3;
    --cream-deep: #ece7d3;
    --ink: #111111;
    --emblem-light: #c7aa9c;
    --emblem-dark: #9b7a6b;
    --ornament-light: #bfb3a3;
    --ornament-dark: #7f7163;
    --divider: #3a3530;
  }
  * { margin: 0; padding: 0; box-sizing: border-box; }
  html, body {
    width: 1200px;
    height: 742px;
    overflow: hidden;
    background: var(--cream-deep);
  }
  .card {
    position: relative;
    width: 1200px;
    height: 742px;
    overflow: hidden;
    background: radial-gradient(ellipse at 55% 40%, var(--cream-light) 0%, #f6f2e2 55%, var(--cream-deep) 100%);
    color: var(--ink);
  }
  .emblem {
    position: absolute;
    left: 48px;
    top: 88px;
    width: 246px;
    height: 322px;
    border-radius: 40% 40% 18% 18%;
    background: radial-gradient(ellipse at 50% 45%, var(--emblem-light) 0%, var(--emblem-dark) 100%);
    opacity: 0.75;
  }
  .divider {
    position: absolute;
    left: 344px;
    top: 76px;
    width: 4px;
    height: 584px;
    border-radius: 2px;
    background: linear-gradient(to bottom, transparent 0%, var(--divider) 12%, var(--divider) 88%, transparent 100%);
    box-shadow: 6px 0 12px rgba(60, 50, 40, 0.35);
  }
  .firm {
    position: absolute;
    left: 370px;
    width: 800px;
    text-align: center;
  }
  .firm-name {
    top: 108px;
    font-family: "Libre Baskerville", "Bookman Old Style", serif;
    font-weight: 700;
    font-size: 62px;
    line-height: 78px;
    letter-spacing: 0.5px;
  }
  .firm-services {
    top: 308px;
    font-family: "Noto Sans", Verdana, sans-serif;
    font-size: 38px;
    letter-spacing: 1.5px;
  }
  .ornament {
    position: absolute;
    left: 426px;
    top: 390px;
    width: 146px;
    height: 258px;
    border-radius: 50%;
    background: radial-gradient(ellipse at center, var(--ornament-light) 0%, var(--ornament-dark) 100%);
    opacity: 0.55;
  }
  .contact {
    position: absolute;
    left: 590px;
    top: 420px;
    font-family: "Noto Sans", Verdana, sans-serif;
    font-size: 34px;
    line-height: 56.5px;
    letter-spacing: 1.5px;
    list-style: none;
  }
</style>
</head>
<body>
  <div class="card">
    <div class="emblem" role="img" aria-label="Scales of justice emblem in soft mauve"></div>
    <div class="divider"></div>
    <h1 class="firm firm-name">Helena Brackett<br>&amp; Associates</h1>
    <p class="firm firm-services">Lawyers &amp; Conveyancers</p>
    <div class="ornament" role="img" aria-label="Decorative scrolled flourish"></div>
    <ul class="contact">
      <li>Helena Brackett</li>
      <li>LL.B. Principal Solicitor</li>
      <li>17 Quillon Street</li>
      <li>Marrowdale NSW 2190</li>
    </ul>
  </div>
</body>
</html>
```